Business Cards for Tax Preparation Business
KRT Tax Preparation
Business Cards for Tax Preparation Business - Financial Services
Creative Brief
Cutting-Edge
Brian K Holloway
Registered Tax Return Preparer
47 Birchmont Avenue, Suite 318 Maple Glen, ST 00000
860-555-0148 x36
brian@krtfiling.example
www.krtfiling.example

```html
<!DOCTYPE html>
<html lang="en">
<head>
<meta charset="utf-8">
<title>KRT Tax Preparation – Business Cards</title>
<link href="https://fonts.googleapis.com/css2?family=Cinzel:wght@600&family=Crimson+Text:wght@400;600&display=swap" rel="stylesheet">
<style>
  :root {
    --backdrop: #e9e7e3;
    --card-white: #ffffff;
    --card-black: #0b0b0c;
    --card-black-soft: #1c1c1f;
    --navy: #27348b;
    --navy-bright: #3a4bb8;
    --gold-dark: #a88a1f;
    --gold: #d8bb45;
    --gold-light: #f1de86;
    --text-light: #e8e8e8;
    --text-muted: #c4c4c4;
  }
  * { margin: 0; padding: 0; box-sizing: border-box; }
  html, body { width: 1200px; height: 901px; overflow: hidden; }
  body {
    background: var(--backdrop);
    position: relative;
    font-family: "Crimson Text", Georgia, serif;
  }
  .card {
    position: absolute;
    left: 250px;
    width: 700px;
    height: 400px;
    border-radius: 14px;
    overflow: hidden;
    box-shadow: 0 6px 18px rgba(0,0,0,0.18);
  }
  .brand { display: flex; align-items: center; gap: 12px; }
  .brand-mark { width: 14px; height: 14px; background: var(--navy); flex: none; }
  .brand-name {
    font-family: "Cinzel", "Times New Roman", serif;
    font-weight: 600;
    color: var(--navy);
    letter-spacing: 1px;
    white-space: nowrap;
  }

  /* Back of card */
  .card-back {
    top: 40px;
    background: linear-gradient(135deg, var(--card-black-soft) 0%, var(--card-black) 60%);
  }
  .card-back .brand { position: absolute; right: 44px; bottom: 56px; }
  .card-back .brand-name { font-size: 30px; color: var(--navy-bright); }
  .card-back .brand-mark { background: var(--navy-bright); }

  /* Front of card */
  .card-front { top: 461px; background: var(--card-black); }
  .front-top {
    position: absolute;
    inset: 0 0 auto 0;
    height: 212px;
    background: var(--card-white);
  }
  .card-front .brand { position: absolute; left: 150px; top: 82px; gap: 14px; }
  .card-front .brand-name { font-size: 38px; }

  .gold-band {
    position: absolute;
    left: 0; right: 0;
    top: 212px;
    height: 42px;
    background: linear-gradient(90deg, var(--gold-dark) 0%, var(--gold) 35%, var(--gold-light) 65%, var(--gold) 100%);
    display: flex;
    align-items: center;
    padding-left: 190px;
  }
  .person {
    color: #ffffff;
    font-size: 18px;
    font-weight: 600;
    letter-spacing: 0.3px;
    white-space: nowrap;
  }
  .person .divider { margin: 0 8px; }

  .contact {
    position: absolute;
    left: 200px;
    top: 268px;
    width: 360px;
    color: var(--text-light);
    font-size: 14px;
    line-height: 1.35;
    text-align: center;
  }
  .contact .lines { margin-top: 6px; color: var(--text-muted); }
  .website {
    position: absolute;
    left: 200px;
    width: 360px;
    bottom: 22px;
    text-align: center;
    color: var(--text-light);
    font-size: 15px;
  }
</style>
</head>
<body>
  <section class="card card-back" aria-label="Card back">
    <div class="brand">
      <span class="brand-mark"></span>
      <span class="brand-name">KRT Tax Preparation</span>
    </div>
  </section>

  <section class="card card-front" aria-label="Card front">
    <div class="front-top">
      <div class="brand">
        <span class="brand-mark"></span>
        <span class="brand-name">KRT Tax Preparation</span>
      </div>
    </div>
    <div class="gold-band">
      <p class="person">Brian K Holloway<span class="divider">|</span>Registered Tax Return Preparer</p>
    </div>
    <div class="contact">
      <p class="address">47 Birchmont Avenue, Suite 318<br>Maple Glen, ST 00000</p>
      <div class="lines">
        <p>P: 860-555-0148 x36 &nbsp;|&nbsp; C: 860-555-0172</p>
        <p>F: 860-555-0191 &nbsp;|&nbsp; E: brian@krtfiling.example</p>
      </div>
    </div>
    <p class="website">www.krtfiling.example</p>
  </section>
</body>
</html>
```